Company brochure for our unique consulting business

We are a small consulting business offering a unique set of services to our clients.. In simple terms we are a business improvement consultancy helping our clients get the best out of their businesses. We work with clients across multiple sectors and deliver a variety of services. We want to put together a brochure to cover these main themes:1. Who we are2. What we do3. The type of people we employ4. The sectors we work inWhile the brochure needs to have a certain corporate feel to it, we don't want it to be "boring" or "stiff". We would like it to have a slightly "friendly" or "informal" feel to it, to reflect the type of organisation we are.We have a company website http://tollandvergeadvisory.com , however we do not want to directly replicate the content or feel as we recognise it needs updating.We would like the brochure to be A4 portrait format. We anticipate requiring 12 sides (including covers) but we are happy to be guided on this based on the content we have provided.The attached ppt file gives the detail of the content to be included and also shows the proposed pagination. For the front cover we would like to try 2 versions, one with the TVA logo and one with the Tolland Verge Advisory logo (a file of both is attached)One of the most important pages will be the "Our Services" page. We would like this to cover the centre fold. In the ppt file we have shown an example layout, but this is where we need most help - we are clearly not graphic designers! This page will be the most used page in sales meetings etc.Also attached is the following:1. file for our TollandVerge Advisory company logo.2. File for our TVA company logo3. Files for Derek's signatures (for under photos) - Owen's to follow4. Photo of Derek & Owen (person in purple shirt to be cropped out)Thank you and really excited to see what everyone comes back with.Derek & Owen

Target Market(s)

Very broad - Manufacturing, Healthcare, Hospitality

Industry/Entity Type

Management Consulting

Font styles to use
Other font styles liked:
• We use Swiss721, but happy to be guided by designer

Colors
3276b5
85abd2
0355a3
333333
5c5c5c
9d9d9d
d9d9d9

Requirements
Must have
• Corporate feel
Nice to have
• Slightly friendly feel
• Our standard "blue" is (CORRECTION) - R55 G96 B146 #376092 and our standard grey is R197 G178, B179 - #B3B2B2, which we would like to keep, but other colours we are happy to be guided on. Brand guidelines attached.

```html
<!DOCTYPE html>
<html lang="en">
<head>
<meta charset="utf-8">
<title>Tolland Verge Advisory – Brochure Spread</title>
<link href="https://fonts.googleapis.com/css2?family=Lato:wght@400;700;900&display=swap" rel="stylesheet">
<style>
  :root{
    --brand-blue:#376092;
    --blue-mid:#3276b5;
    --blue-light:#85abd2;
    --ink:#333333;
    --ink-soft:#5c5c5c;
    --grey:#9d9d9d;
    --paper:#f4f5f6;
    --backdrop:#e3e3e3;
  }
  *{box-sizing:border-box;margin:0;padding:0}
  html,body{width:1200px;height:939px;overflow:hidden;background:var(--backdrop);font-family:'Lato',sans-serif;color:var(--ink)}
  .spread{position:absolute;left:40px;top:75px;width:1120px;height:790px;display:flex;box-shadow:0 10px 30px rgba(0,0,0,.18)}
  .page{position:relative;width:560px;height:790px;background:linear-gradient(180deg,#fbfbfb,var(--paper));overflow:hidden}
  .page--left{border-right:1px solid #d6d6d6}
  .page svg.art{position:absolute;left:0;top:0}
  .wordmark{position:absolute;display:flex;align-items:center;gap:8px;color:#fff;font-weight:900;font-size:44px;letter-spacing:1px;line-height:1}
  .wordmark .mark{width:16px;height:16px;background:#fff}
  .wordmark--right{right:30px;top:34px;font-size:40px}
  .section-title{position:absolute;display:flex;align-items:center;gap:8px;color:var(--brand-blue);font-weight:900;font-size:30px;text-transform:uppercase;letter-spacing:.5px;line-height:1}
  .section-title::before{content:"";width:12px;height:26px;background:var(--brand-blue)}
  .values{position:absolute;left:40px;top:520px;width:490px;list-style:none;font-size:12px;line-height:1.55;color:var(--ink-soft)}
  .values li{position:relative;padding-left:16px;margin-bottom:4px}
  .values li::before{content:"";position:absolute;left:0;top:5px;width:7px;height:7px;background:var(--brand-blue)}
  .values strong{color:var(--brand-blue);font-weight:900;text-transform:uppercase}
  .company-name{position:absolute;left:40px;top:130px;width:180px;font-weight:900;font-size:21px;line-height:1.1;color:var(--ink)}
  .intro{position:absolute;left:240px;top:150px;width:280px;font-size:12px;line-height:1.45;color:var(--ink-soft)}
  .accent-bar{position:absolute;left:40px;top:215px;width:50px;height:260px;background:var(--brand-blue)}
  .accent-bar--short{top:540px;height:24px;width:60px}
  .signature{position:absolute;height:50px;background:linear-gradient(90deg,rgba(51,51,51,.08),rgba(51,51,51,.18))}
  .expertise{position:absolute;left:110px;top:598px;width:420px;font-size:12px;line-height:1.45;color:var(--ink-soft)}
</style>
</head>
<body>
<main class="spread">

  <section class="page page--left">
    <svg class="art" width="560" height="790" viewBox="0 0 560 790">
      <defs>
        <linearGradient id="bandBlue" x1="0" y1="0" x2="1" y2="1">
          <stop offset="0" stop-color="#4b77a8"/><stop offset="1" stop-color="#2e5583"/>
        </linearGradient>
        <linearGradient id="handPhoto" x1="0" y1="0" x2="1" y2="1">
          <stop offset="0" stop-color="#2a2a2c"/><stop offset=".5" stop-color="#5a5450"/><stop offset="1" stop-color="#8a8682"/>
        </linearGradient>
      </defs>
      <path d="M0 0H560V120Q300 70 0 150Z" fill="url(#bandBlue)"/>
      <path d="M0 150Q300 70 560 120V150Q300 100 0 180Z" fill="#c9ccd0"/>
      <path d="M0 180Q300 100 560 150V420Q300 420 0 470Z" fill="url(#handPhoto)" role="img" aria-label="Photo of a businessman in a dark suit giving a thumbs up"/>
    </svg>
    <div class="wordmark" style="left:230px;top:40px"><span class="mark"></span>TVA</div>
    <h2 class="section-title" style="left:40px;top:482px">Our Values</h2>
    <ul class="values">
      <li>Be <strong>trusted</strong> by our team and clients, so that our opinions are sought, and our recommendations valued.</li>
      <li>Have a tight knit relationship with our clients, so we are seen as a <strong>partner</strong> and not just supplier.</li>
      <li>Be focused on return-on-investment, but predominantly, always deliver <strong>great value</strong>.</li>
      <li><strong>Develop &amp; invest in</strong> our own people to continually stay one step ahead.</li>
      <li>Work relentlessly to deliver results for our clients, but ensure we collectively <strong>enjoy the journey</strong>.</li>
      <li>Take <strong>social responsibility</strong> seriously by supporting other worthwhile organisations.</li>
    </ul>
  </section>

  <section class="page page--right">
    <svg class="art" width="560" height="790" viewBox="0 0 560 790">
      <defs>
        <linearGradient id="bandBlue2" x1="0" y1="0" x2="1" y2="1">
          <stop offset="0" stop-color="#4b77a8"/><stop offset="1" stop-color="#2e5583"/>
        </linearGradient>
        <linearGradient id="teamPhoto" x1="0" y1="0" x2="1" y2="1">
          <stop offset="0" stop-color="#efe9df"/><stop offset=".55" stop-color="#9fb9d8"/><stop offset="1" stop-color="#d9cbb4"/>
        </linearGradient>
        <linearGradient id="mapFill" x1="0" y1="0" x2="1" y2="1">
          <stop offset="0" stop-color="#2f6396"/><stop offset="1" stop-color="#376092"/>
        </linearGradient>
      </defs>
      <path d="M0 0H560V170Q440 40 0 30Z" fill="url(#bandBlue2)"/>
      <path d="M0 30Q440 40 560 170V188Q440 58 0 46Z" fill="#c9ccd0"/>
      <rect x="90" y="230" width="440" height="300" fill="url(#teamPhoto)" role="img" aria-label="Photo of the two founders smiling at a meeting table"/>
      <rect x="280" y="665" width="250" height="110" rx="4" fill="url(#mapFill)" opacity=".9" role="img" aria-label="World map marking the regions served"/>
    </svg>
    <div class="wordmark wordmark--right"><span class="mark"></span>TVA</div>
    <h2 class="section-title" style="left:34px;top:78px">About Us</h2>
    <div class="company-name">Tolland Verge Advisory</div>
    <p class="intro">At TVA we constantly strive to deliver the best possible value for our clients. Importantly we recognize, it's our clients that define value, not us.</p>
    <div class="accent-bar"></div>
    <div class="accent-bar accent-bar--short"></div>
    <div class="signature" style="left:130px;top:540px;width:150px" role="img" aria-label="Owen's signature"></div>
    <div class="signature" style="left:340px;top:540px;width:170px" role="img" aria-label="Derek's signature"></div>
    <p class="expertise">We bring together our expertise from Hollenfeld Motors and our experience of working with multiple organisations to help our clients deliver results against their own individual goals.</p>
    <h2 class="section-title" style="left:34px;top:690px">Our Regions</h2>
  </section>

</main>
</body>
</html>
```